India Export Business Card Design

We are a small company importing from India,
Antique furniture and textiles.
We would like a design with somthing of India in it.
IE: Camels, Tuk Tuks, People or maybe Taj Mahal.
Only one of the above suggestions, we do not want the card to be to busy.
We travel to India twice a year to get the product and then come home to New Zealand and sell it.
And must have our business name which is
Velmora Trading Company
Nz phone no. 64 9 317 6825
Mobile 64 21 573 162
Email bethany@velmoratrading.co.nz
Www.velmoratrading.co.nz

Also my name and position
Bethany Crowhurst
Director

Reason: I am awaiting for a design to come back with different colours. Many thanks

Target Market(s)

Indian heritage furniture and textiles in India also
New Zealand market for public to buy the goods that is bought in India

Industry/Entity Type

Travel

Contact Information for Business Card

Velmora Trading Company
17b Harlow Lane
RD 7 Papakura 2590
Auckland
New Zealand
email address which will be associated to our new website
website once we have it assigned

Requirements
Must have
• Company name and region.
Phone numbers
My name and title.
Nice to have
• I would like the card to portray India and as i said before, I like the idea of camels in a line with ropes between them like an animation.
But happy to see what other suggestions there are.

```html
<!DOCTYPE html>
<html lang="en">
<head>
<meta charset="utf-8">
<title>Velmora Trading Company – Business Cards</title>
<link href="https://fonts.googleapis.com/css2?family=Jost:wght@400;500&display=swap" rel="stylesheet">
<style>
  :root {
    --backdrop: #a9a9a9;
    --card: #efefef;
    --accent: #3896bd;
    --ink: #2b2b2b;
  }
  * { box-sizing: border-box; margin: 0; padding: 0; }
  html, body {
    width: 1200px; height: 899px; overflow: hidden;
    background: var(--backdrop);
    font-family: "Jost", "Futura", sans-serif;
  }
  .card {
    position: absolute;
    width: 630px; height: 360px;
    background: var(--card);
    box-shadow: 0 4px 10px rgba(0,0,0,0.25);
  }
  .tab {
    position: absolute;
    width: 14px;
    background: var(--accent);
    border-radius: 7px;
  }
  /* Front card */
  .card--front { left: 90px; top: 50px; }
  .card--front .tab--left { left: -7px; top: 120px; height: 160px; }
  .card--front .tab--right { right: -7px; top: 80px; height: 150px; }
  .brand {
    position: absolute; left: 80px; top: 70px;
    display: flex; align-items: center; gap: 28px;
  }
  .brand__mark {
    width: 100px; height: 80px;
    background: var(--accent);
  }
  .brand__name {
    color: var(--accent);
    font-size: 30px; font-weight: 500;
  }
  .front-contact {
    position: absolute; left: 0; right: 0; top: 240px;
    text-align: center; color: var(--ink);
    font-size: 26px; line-height: 1.15; letter-spacing: 0.5px;
  }
  /* Back card */
  .card--back { left: 500px; top: 480px; }
  .card--back .tab--left { left: -7px; top: 40px; height: 150px; }
  .card--back .tab--right { right: -7px; top: 210px; height: 130px; }
  .back-brand {
    position: absolute; left: 50px; top: 34px;
    display: flex; align-items: center; gap: 10px;
    color: var(--accent); font-size: 20px; font-weight: 500;
  }
  .back-brand__mark { width: 18px; height: 18px; background: var(--accent); }
  .person {
    position: absolute; left: 0; right: 0; top: 150px;
    text-align: center; color: var(--ink);
  }
  .person__name { color: var(--accent); font-size: 38px; font-weight: 500; line-height: 1.1; }
  .person__title { font-size: 32px; line-height: 1.1; }
  .person__phone, .person__email { font-size: 19px; line-height: 1.3; }
</style>
</head>
<body>
  <section class="card card--front">
    <span class="tab tab--left"></span>
    <span class="tab tab--right"></span>
    <div class="brand">
      <span class="brand__mark"></span>
      <span class="brand__name">Velmora Trading Company</span>
    </div>
    <div class="front-contact">
      <p>velmoratrading.co.nz</p>
      <p>64 9 317 6825</p>
    </div>
  </section>

  <section class="card card--back">
    <span class="tab tab--left"></span>
    <span class="tab tab--right"></span>
    <div class="back-brand">
      <span class="back-brand__mark"></span>
      <span>Velmora</span>
    </div>
    <div class="person">
      <p class="person__name">Bethany Crowhurst</p>
      <p class="person__title">Director</p>
      <p class="person__phone">64 21 573 162</p>
      <p class="person__email">bethany@velmoratrading.co.nz</p>
    </div>
  </section>
</body>
</html>
```